TRENDY & MODERN BUSINESS CARD DESIGN for Media Company *

I need a minimalistic - clean - modern and professional business card layout and design for MEDIA & PHOTOGRAPHY STUDIO.

We do NOT have a logo, and not really looking for one - but rather excellent typography and design. We would consider the 3 as a focal point.

We do personal and commercial photography.

Target Market(s)

Personal and commercial photography clientele

Contact Information for Business Card

ZUB size - from zub.com / size guidelines are enclosed in the brief

Font styles to use
Sans Serif

Colors
f78f20
eda3c7
cee9f5
0555a3
e667a6
fbf289

Requirements
Must have
• Clean lines - Modern layout
Nice to have
• All blue background as an option - use color palette in brief please.
Should not have
• Old fashion fonts and regular fonts.

```html
<!DOCTYPE html>
<html lang="en">
<head>
<meta charset="UTF-8">
<title>Lensline Media – Business Card</title>
<link href="https://fonts.googleapis.com/css2?family=Lato:wght@400;700&display=swap" rel="stylesheet">
<style>
  :root {
    --brand-blue: #0f57a6;
    --brand-orange: #f78f20;
    --ink: #111111;
    --ink-soft: #444444;
    --paper: #ffffff;
    --backdrop-light: #5a5a5c;
    --backdrop-dark: #26272a;
  }
  * { margin: 0; padding: 0; box-sizing: border-box; }
  html, body { width: 1200px; height: 900px; overflow: hidden; }
  body {
    background: radial-gradient(ellipse at 60% 35%, var(--backdrop-light), var(--backdrop-dark) 75%);
    font-family: "Lato", sans-serif;
    position: relative;
  }
  .card {
    position: absolute;
    width: 500px;
    height: 286px;
    border-radius: 26px;
    overflow: hidden;
    box-shadow: 0 18px 40px rgba(0,0,0,0.45);
  }
  /* Front */
  .card-front {
    left: 90px; top: 150px;
    background: var(--brand-blue);
    display: flex; align-items: center; justify-content: center;
  }
  .brand-name {
    font-size: 40px; font-weight: 400; letter-spacing: 2px;
    text-transform: uppercase; line-height: 1;
    color: var(--brand-orange);
    white-space: nowrap;
  }
  /* Back */
  .card-back {
    left: 610px; top: 464px;
    background: var(--paper);
  }
  .name-marker {
    position: absolute; left: 0; top: 58px;
    width: 12px; height: 38px; background: var(--brand-blue);
  }
  .person-name {
    position: absolute; left: 28px; top: 52px;
    font-size: 27px; font-weight: 400; color: var(--ink); letter-spacing: 0.5px;
    text-transform: uppercase; line-height: 1;
  }
  .person-title {
    position: absolute; left: 28px; top: 80px;
    font-size: 15px; color: var(--ink-soft); letter-spacing: 0.8px;
    text-transform: uppercase;
  }
  .contact-list {
    position: absolute; left: 40px; top: 128px;
    list-style: none; font-size: 15px; color: var(--ink); line-height: 1.2;
  }
  .contact-list li { display: flex; align-items: flex-start; gap: 14px; margin-bottom: 8px; }
  .contact-list svg { width: 16px; height: 16px; flex: none; margin-top: 2px; fill: var(--ink); }
  .city-band {
    position: absolute; left: 0; bottom: 0; width: 100%; height: 34px;
    background: var(--brand-blue);
    display: flex; align-items: center; justify-content: space-evenly;
    color: var(--paper); font-size: 15px;
  }
  .city-band .sep { font-size: 10px; }
</style>
</head>
<body>

<section class="card card-front">
  <h1 class="brand-name">Lensline Media</h1>
</section>

<section class="card card-back">
  <div class="name-marker"></div>
  <h2 class="person-name">Marisol Vega</h2>
  <p class="person-title">Founder &amp; Media Director</p>

  <ul class="contact-list">
    <li>
      <svg viewBox="0 0 24 24" aria-hidden="true"><path d="M12 2a7 7 0 0 0-7 7c0 5 7 13 7 13s7-8 7-13a7 7 0 0 0-7-7zm0 9.5a2.5 2.5 0 1 1 0-5 2.5 2.5 0 0 1 0 5z"/></svg>
      <span>2240 Coral Way<br>4th Floor<br>Miami, FL 33145</span>
    </li>
    <li>
      <svg viewBox="0 0 24 24" aria-hidden="true"><path d="M6.6 10.8a15 15 0 0 0 6.6 6.6l2.2-2.2a1 1 0 0 1 1-.25 11.4 11.4 0 0 0 3.6.57 1 1 0 0 1 1 1V20a1 1 0 0 1-1 1A17 17 0 0 1 3 4a1 1 0 0 1 1-1h3.5a1 1 0 0 1 1 1c0 1.25.2 2.45.57 3.6a1 1 0 0 1-.25 1z"/></svg>
      <span>(305) 555-0142</span>
    </li>
    <li>
      <svg viewBox="0 0 24 24" aria-hidden="true"><path d="M2 21l21-9L2 3v7l15 2-15 2z"/></svg>
      <span>mv@lenslinemedia.com</span>
    </li>
  </ul>

  <div class="city-band">
    <span>Miami</span><span class="sep">•</span>
    <span>New York</span><span class="sep">•</span>
    <span>Las Vegas</span><span class="sep">•</span>
    <span>Cancun</span><span class="sep">•</span>
    <span>Roma</span>
  </div>
</section>

</body>
</html>
```